Muslim funeral brochure for Swedish market

Purpose of the brochure: We are a new funeral home in Sweden. We are launching a funeral guide for muslim funerals in Sweden in order to develop credibility. We will create a brochure that describe how a muslim funeral is conducted in Sweden and aspects that are important for the relatives of the deceased to understand.

Size of the brochure: We are hoping that muslim associations in Sweden will have our brochure on their website and that they should have a link from where the brochure should be downloaded. Is should be possible to print the brochure on a regular printer. We will most likely print the brochure and for this purpose it would be helpful if the brochure is constructed in an attractive format.

Content: We have attached a preliminary text intended for our brochure. The attached pdf is not indicative for how we would like the end product to look like.

This URL:

http://blogg.vardagsnytt-exempel.se/lisbethk/files/2013/11/infographic-tornvik.jpeg-page.jpg

goes to a brochure we found on the web that describes child car safety that a company is using to get authority to sell more car seats (maybe we can use this for inspiration)
Updates

Please note that the design in the pdf I attached to the project brief should not be indicative for how I would like the end product to look like. It is a scetch I did to communicate content to the designers of pixel forum. I am hoping for a more appealing design eg the URL I attached in the brief is a good example of how a boring subject was communicated in an appealing way.Thanks Gunnar Added Friday, October 30, 2015

Target Market(s)

Muslims in Sweden

Industry/Entity Type

Funeral Home

Font styles to use
Sans Serif

Colors
00a990

Requirements
Must have
• *Relevant illustrations
• *Enough space so that we can translate into several languages without changing design
• *A format that we ourselves can change in case needed
• *Brochure use same colors and design (if possible and unless the designer has some better ideas) as we do on our web page www.lundagravbyra-exempel.se.
• *Should be possible to create a print friendly version of the flyer with less colors
Nice to have
• Suggestions of which brochure formats we should use in order to make it:
• *Attractive for professional print
• *Print friendly format for home users
Should not have
• Symbols specific to a certain fraction of islam e.g. sunni, shia muslim and ISIS

```html
<!DOCTYPE html>
<html lang="sv">
<head>
<meta charset="utf-8">
<title>Så utförs en muslimsk begravning i Sverige</title>
<link rel="stylesheet" href="https://fonts.googleapis.com/css2?family=Oswald:wght@500;700&family=Lato:wght@400;700;900&display=swap">
<style>
  :root{
    --teal:#1ba58e;
    --teal-dark:#245a60;
    --ink:#2c2c2c;
    --grey-band:#ececec;
    --swoosh-dark:#3a3a3a;
    --paper:#ffffff;
  }
  *{box-sizing:border-box;margin:0;padding:0}
  html,body{width:907px;height:1200px;overflow:hidden;background:var(--paper)}
  body{font-family:"Lato",sans-serif;color:var(--ink);position:relative}

  .flyer{position:relative;width:907px;height:1200px;overflow:hidden;background:var(--paper)}

  .header-art{position:absolute;left:0;top:0;width:907px;height:360px}

  .title{position:absolute;right:40px;top:52px;text-align:right;font-family:"Oswald",sans-serif;font-weight:700;color:#fff;font-size:40px;letter-spacing:.5px;line-height:1}
  .subtitle{position:absolute;right:40px;top:173px;font-family:"Oswald",sans-serif;font-weight:500;color:#2a2a2a;font-size:25px;letter-spacing:.8px;line-height:1}

  .intro{position:absolute;left:365px;top:268px;width:500px;font-size:12px;line-height:1.5;text-align:justify}

  .timeline-label{position:absolute;left:0;top:350px;width:907px;height:30px}
  .timeline-label .rule{position:absolute;top:14px;height:2px;background:var(--teal-dark)}
  .timeline-label .rule.left{left:220px;width:140px}
  .timeline-label .rule.right{left:548px;width:140px}
  .timeline-label .arrowhead{position:absolute;top:9px;width:0;height:0;border-top:6px solid transparent;border-bottom:6px solid transparent}
  .timeline-label .arrowhead.left{left:208px;border-right:12px solid var(--teal-dark)}
  .timeline-label .arrowhead.right{left:688px;border-left:12px solid var(--teal-dark)}
  .timeline-label h2{position:absolute;left:360px;width:188px;text-align:center;font-family:"Oswald",sans-serif;font-weight:700;color:var(--teal-dark);font-size:20px;line-height:30px}

  .step{position:absolute;text-align:center;font-weight:700;font-size:12px;line-height:1.35;color:#222}
  .step svg{display:block;margin:0 auto 8px}
  .step p{overflow-wrap:anywhere;word-break:break-word}
  .step.home{left:140px;top:398px;width:160px}
  .step.hospital{left:362px;top:398px;width:195px}
  .step.mosque{left:640px;top:390px;width:150px}

  .flow-arrow{position:absolute}
  .flow-arrow.one{left:312px;top:428px}
  .flow-arrow.two{left:570px;top:428px}

  .divider{position:absolute;left:40px;top:597px;width:827px;height:4px;background:linear-gradient(90deg,rgba(27,165,142,.35),var(--teal),rgba(27,165,142,.35))}

  .columns{position:absolute;left:40px;top:630px;width:827px;display:flex;gap:30px}
  .col{flex:1}
  .fact{position:relative;padding-left:14px;margin-bottom:12px;font-size:11.2px;line-height:1.42;text-align:justify}
  .fact::before{content:"";position:absolute;left:0;top:6px;width:5px;height:5px;border-radius:50%;background:var(--teal-dark)}
  .fact strong{font-weight:900;color:var(--teal-dark);font-size:12.5px;letter-spacing:.2px}

  .brand{position:absolute;left:95px;top:930px;width:260px;display:flex;flex-direction:column;align-items:center}
  .brand .name{font-family:"Lato",sans-serif;font-weight:900;font-size:24px;letter-spacing:2px;color:var(--teal-dark);line-height:1;white-space:nowrap}
  .brand .dot{width:12px;height:12px;border-radius:50%;background:var(--teal-dark);margin-bottom:10px}

  .contact{position:absolute;left:482px;top:896px;font-weight:900;color:#1e1e1e}
  .contact li{list-style:none;display:flex;align-items:center;gap:10px;font-size:15.5px;margin-bottom:10px}
  .contact li.phone{font-family:"Oswald",sans-serif;font-weight:500;font-size:30px;color:var(--teal);margin-bottom:8px}
  .contact svg{flex:none}

  .skyline{position:absolute;left:0;bottom:0;width:907px;height:190px;background:linear-gradient(180deg,rgba(36,90,96,0) 0%,rgba(36,90,96,.55) 35%,var(--teal-dark) 70%)}
</style>
</head>
<body>
<main class="flyer">

  <svg class="header-art" viewBox="0 0 907 360">
    <defs>
      <linearGradient id="photoTone" x1="0" y1="0" x2="1" y2="1">
        <stop offset="0" stop-color="#a8b98a"/>
        <stop offset=".5" stop-color="#cfc2a3"/>
        <stop offset="1" stop-color="#b7a787"/>
      </linearGradient>
    </defs>
    <g role="img" aria-label="Fotografi av gamla gravstenar på en muslimsk begravningsplats">
      <path d="M0 0 H450 V40 C425 140 380 215 330 252 C260 290 150 342 0 342 Z" fill="url(#photoTone)"/>
    </g>
    <path class="banner" d="M450 30 H907 V160 H560 C500 160 440 200 395 238 C420 150 435 90 450 30 Z" fill="var(--teal)"/>
    <path class="band" d="M520 162 H907 V220 H505 C505 195 510 175 520 162 Z" fill="var(--grey-band)"/>
    <path d="M0 342 C150 342 260 290 330 252 C370 234 600 232 907 232" fill="none" stroke="var(--teal)" stroke-width="5"/>
    <path d="M0 353 C150 353 270 300 340 263 C380 245 600 245 907 245" fill="none" stroke="var(--swoosh-dark)" stroke-width="4"/>
  </svg>

  <h1 class="title">SÅ UTFÖRS EN MUSLIMSK</h1>
  <p class="subtitle">BEGRAVNING I SVERIGE</p>

  <p class="intro">Muslimer kommer från olika länder, har skilda språk och olika kulturbakgrund. Därförkan det finnas olika församlingar där regler och traditioner i samband med begravning skiljer sig åt. Muslimer skall alltid jordbegravas och begravningsplatsens gravar skall läggas så att den döde ligger vänd mot Mekka.</p>

  <div class="timeline-label">
    <span class="arrowhead left"></span><span class="rule left"></span>
    <h2>INOM 36 TIMMER</h2>
    <span class="rule right"></span><span class="arrowhead right"></span>
  </div>

  <div class="step home">
    <svg width="110" height="80" viewBox="0 0 110 80" fill="none" stroke="var(--teal-dark)" stroke-width="4">
      <path d="M14 38 L55 8 L96 38"/><path d="M78 24 V6 H88 V31"/>
      <rect x="26" y="34" width="58" height="38"/>
      <rect x="33" y="44" width="14" height="12"/><rect x="60" y="46" width="14" height="26"/>
      <path d="M4 52 V76 M12 52 V76 M98 52 V76 M106 52 V76 M2 60 H26 M2 70 H26 M84 60 H108 M84 70 H108"/>
    </svg>
    <p>Inträffar dödsfallet i t.ex. hemmet eller pååldomshem transporteras kroppen till ett sjukhus.</p>
  </div>

  <svg class="flow-arrow one" width="50" height="36" viewBox="0 0 50 36" fill="none" stroke="var(--teal-dark)" stroke-width="2.5" stroke-linejoin="round">
    <path d="M4 32 C8 18 18 12 30 12 V4 L46 16 L30 28 V20 C20 20 12 24 4 32 Z"/>
  </svg>

  <div class="step hospital">
    <svg width="100" height="82" viewBox="0 0 100 82" fill="none" stroke="var(--teal-dark)" stroke-width="4">
      <rect x="14" y="6" width="72" height="72"/>
      <path d="M50 14 V40 M37 27 H63" stroke-width="7"/>
      <path d="M4 78 H96"/>
      <rect x="24" y="50" width="10" height="8"/><rect x="45" y="50" width="10" height="8"/><rect x="66" y="50" width="10" height="8"/>
      <rect x="24" y="64" width="10" height="8"/><rect x="45" y="64" width="10" height="8"/><rect x="66" y="64" width="10" height="8"/>
    </svg>
    <p>Dödsorsak fastställs ochinnan kroppen lämnarbårhuset genom-försenreligiöstvagningsceremoniva-refterdendödelindasbomullstyg.Und er ceemonindeltar en Imam samt rep-resentantfrånbegravningsbyrån.</p>
  </div>

  <svg class="flow-arrow two" width="50" height="36" viewBox="0 0 50 36" fill="none" stroke="var(--teal-dark)" stroke-width="2.5" stroke-linejoin="round">
    <path d="M4 4 C8 18 18 24 30 24 V32 L46 20 L30 8 V16 C20 16 12 12 4 4 Z"/>
  </svg>

  <div class="step mosque">
    <svg width="100" height="92" viewBox="0 0 100 92" fill="none" stroke="var(--teal-dark)" stroke-width="4">
      <path d="M12 88 V28 M88 88 V28 M7 28 H17 M83 28 H93 M12 28 L12 14 M88 28 L88 14"/>
      <path d="M30 50 C30 30 50 28 50 12 C50 28 70 30 70 50 Z"/>
      <rect x="26" y="50" width="48" height="38"/>
      <path d="M43 88 V72 C43 64 57 64 57 72 V88"/>
      <path d="M2 88 H98"/>
    </svg>
    <p>Begravningen sker efter middagsbönen. Den inleds med en kort bön och sedan följer männen med till begravningsplatsen. De hjälps åt att lägga den</p>
  </div>

  <div class="divider"></div>

  <section class="columns">
    <div class="col">
      <p class="fact"><strong>BEGRAVNING INOM 36 TIMMAR</strong> - Enligt islam skall den döde begravas så snart som möjligt -helst inom 36 timmar. På grund av de administrativa handläggningstiderna i Sverige är detinte alltid möjligt att utföra begravningen inom 36 timmar. möjligt kan anhöriga be jourhavande läkare att utfärda och skickadödsintyg till skatteverket så snabbt som möjligt då de vill begrava den avlidne enligtmuslimsk sed dvs. inom 36 timmar</p>
      <p class="fact"><strong>EN ENKEL KISTA</strong> - I muslimska länder är det vanligt att den avlidne begravs utan kista ochendast inlindad i bomullstyg. I samband med en jordbegravning i Sverige måste den avlidnelligga i en kista.</p>
      <p class="fact"><strong>DIN ISLAMISKA FÖRSAMLING</strong> - De flesta utövare av islam i Sverige tillhör en Islamiskförsamling. Din församling tillhandahåller en Imam som deltar vid den religiösatvagningsceremonin. I vissa fall kan anhöriga själva tvaga den avlidne. Församlingen brukardessutom tillhandahålla en Imam som leder begravningsceremonin vid gravplatsen.</p>
    </div>
    <div class="col">
      <p class="fact"><strong>DIN BEGRAVNINGSBYRÅ</strong> - Din begravningsbyrå ansvarar för att samordna transporter ochtillhandahåller en enkel kista som den avlidne kan läggas och begravas i. De flesta bårhuskräver att en representant från begravningsbyrån deltar under den religiösatvagningsceremonin.</p>
      <p class="fact"><strong>GRAVPLATS</strong> - Begravningsplatsens gravar skall läggas så att den döde ligger vänd motMekka. med en enkel gravmarkör som visar var gravens huvudrespektive fotändan finns. En muslimsk grav ska ej beträdas och får inte återanvändas.</p>
      <p class="fact"><strong>UTLANDSBEGRAVNINGAR</strong> -Om man bestämmer sig för att den avlidne ska begravasutomlands tillkommer en del administration och arbete. Intyg som måste sammanställas gravsättningsintyg samt balsamerings-,lödnings-, och transportintyg. I tillägg krävs stämplar från konsulatet vilket hanteras av deanhöriga.</p>
    </div>
  </section>

  <div class="brand">
    <span class="dot"></span>
    <span class="name">LUNDA GRAVBYRÅ</span>
  </div>

  <ul class="contact">
    <li class="phone">
      <svg width="20" height="20" viewBox="0 0 20 20" fill="none" stroke="var(--teal)" stroke-width="2"><circle cx="10" cy="10" r="8.5"/><path d="M7 5 C5 8 8 14 12 15 L13.5 13 L11.5 11.5 L10.5 12.5 C9 11.5 8 10 7.8 9 L9 8 L8 6 Z" fill="var(--teal)" stroke-width="1"/></svg>
      020 – 41 41 41
    </li>
    <li>
      <svg width="20" height="20" viewBox="0 0 20 20" fill="none" stroke="var(--teal-dark)" stroke-width="1.8"><circle cx="10" cy="10" r="8.5"/><ellipse cx="10" cy="10" rx="3.8" ry="8.5"/><path d="M1.5 10 H18.5 M3 5.5 H17 M3 14.5 H17"/></svg>
      www.lundagravbyra-exempel.se
    </li>
    <li>
      <svg width="22" height="16" viewBox="0 0 22 16"><rect width="22" height="16" rx="1.5" fill="var(--teal-dark)"/><path d="M1 1.5 L11 9 L21 1.5" fill="none" stroke="#fff" stroke-width="1.8"/></svg>
      kund@lundagravbyra-exempel.se
    </li>
  </ul>

  <div class="skyline" role="img" aria-label="Silhuett av en stadssiluett med kyrktorn, kupoler och höghus"></div>

</main>
</body>
</html>
```